Design mobile friendly review and ranking site

We're working on a corporate website for reviewing and ranking fellow employees. We need the website to look both fun and professional and it needs to be responsive - to it works on mobile and desktop.

Looking for css and HTML for 3 key pages as well as a header and footer for the site. Also would need any supporting graphics as part of the design.

Target Market(s)

Professionals in their 20s, 30s, and 40s.

Industry/Entity Type

Internet

Coding

Coded - Design and coding required

Number of Pages Required

3 page

Font styles to use
Sans Serif

Requirements
Must have
• 3 key pages we need (note included screenshots for each - these are just super rough cuts so you see examples of the content.)
• a) main-intro: A compelling into page with a login/registration form. Should be sleek/modern/enticing. Also we would show the ranking for the top 3 people to tease people re: content.
• b) main-page: Has two sections: One at the top where you would rate someone and one at the bottom where it shows a ranking of people.
• c) profile page: This is where you view a specific person. You see the person's picture, some info about the person, you see their overall rating, you can rate them, and you also see their historical ratings.
Nice to have
• Note we need css and HTML for this. It should feel as sleek and modern. Note also must be responsive design so it works well in mobile and desktop.

```html
<!DOCTYPE html>
<html lang="en">
<head>
<meta charset="utf-8">
<title>Rankwell – Sign in</title>
<link rel="stylesheet" href="https://fonts.googleapis.com/css2?family=Roboto:ital,wght@0,300;0,400;0,500;0,700;1,300&display=swap">
<style>
  :root {
    --page-bg: #2b2d33;
    --scene-top: #3a3f4a;
    --scene-mid: #525866;
    --scene-low: #6b6466;
    --scene-base: #2a2b30;
    --card: #ffffff;
    --rule: #e6e6e6;
    --ink: #333333;
    --ink-soft: #555555;
    --field-border: #cfcfcf;
    --field-text: #8a8a8a;
    --button: #555555;
    --rank-cell: #1f2024;
    --rating-cell: #efefef;
    --star-on: #f6c712;
    --star-off: #4a4a4a;
    --avatar-a: #c9a98f;
    --avatar-b: #7d6a5e;
  }
  * { box-sizing: border-box; margin: 0; padding: 0; }
  html, body { width: 1200px; height: 1200px; overflow: hidden; }
  body {
    background: var(--page-bg);
    font-family: "Roboto", Arial, sans-serif;
    color: var(--ink);
    position: relative;
  }
  .screen {
    position: absolute;
    left: 0; top: 262px;
    width: 1200px; height: 676px;
    overflow: hidden;
  }
  .screen-backdrop {
    position: absolute; inset: 0;
    background: linear-gradient(180deg, var(--scene-top) 0%, var(--scene-mid) 45%, var(--scene-low) 75%, var(--scene-base) 100%);
  }

  /* Login card */
  .login-card {
    position: absolute;
    left: 99px; top: 105px;
    width: 323px; height: 379px;
    background: var(--card);
    box-shadow: 0 2px 8px rgba(0,0,0,.25);
  }
  .brand {
    height: 58px;
    border-bottom: 1px solid var(--rule);
    display: flex; align-items: center; justify-content: center;
    font-size: 20px; font-weight: 500; color: var(--ink);
    letter-spacing: .2px;
  }
  .intro {
    padding: 24px 26px 0;
    font-size: 12px; line-height: 18px; color: var(--ink-soft);
  }
  .login-form { position: absolute; left: 26px; right: 26px; top: 203px; }
  .field {
    display: block; width: 100%; height: 35px;
    border: 1px solid var(--field-border);
    padding: 0 11px; margin-bottom: 18px;
    font: 400 12px "Roboto", Arial, sans-serif; color: var(--field-text);
    line-height: 33px;
  }
  .sign-in {
    display: block; width: 100%; height: 35px;
    background: var(--button); color: #fff;
    border: 1px solid #3e3e3e;
    font: 500 12px "Roboto", Arial, sans-serif;
    line-height: 33px; text-align: center;
  }

  /* Ranking */
  .ranking { position: absolute; left: 448px; top: 149px; width: 568px; list-style: none; }
  .rank-row {
    display: flex; height: 115px; margin-bottom: 10px;
  }
  .rank-badge {
    width: 155px; background: var(--rank-cell); color: #fff;
    display: flex; align-items: center; padding-left: 17px; gap: 9px;
  }
  .rank-num { font-size: 31px; font-weight: 500; line-height: 1; }
  .rank-num em { font-size: 17px; font-weight: 300; font-style: italic; margin-left: 1px; }
  .avatar {
    width: 80px; height: 80px; border-radius: 50%;
    border: 3px solid #fff;
    background: radial-gradient(circle at 50% 40%, var(--avatar-a), var(--avatar-b));
  }
  .person {
    width: 129px; background: var(--card);
    padding: 26px 10px 0 18px;
  }
  .person h2 { font-size: 16px; font-weight: 400; line-height: 17px; color: var(--ink); margin-bottom: 10px; }
  .person p { font-size: 10px; line-height: 15px; color: var(--ink-soft); }
  .person b { font-weight: 700; color: var(--ink); }
  .ratings {
    flex: 1; background: var(--rating-cell);
    padding: 22px 0 0;
  }
  .rating { display: flex; align-items: center; height: 26px; }
  .rating dt { width: 125px; text-align: right; font-size: 10.5px; color: var(--ink-soft); padding-right: 26px; }
  .stars { display: flex; gap: 2px; }
  .stars svg { width: 15px; height: 15px; }
  .on { fill: var(--star-on); }
  .off { fill: var(--star-off); }
</style>
</head>
<body>
<svg width="0" height="0" style="position:absolute" aria-hidden="true">
  <symbol id="star" viewBox="0 0 24 24"><path d="M12 1.8l3.1 6.9 7.4.7-5.6 5 1.7 7.4L12 17.9l-6.6 3.9 1.7-7.4-5.6-5 7.4-.7z"/></symbol>
</svg>

<main class="screen">
  <div class="screen-backdrop" role="img" aria-label="Blurred city skyline at dusk behind the page"></div>

  <section class="login-card">
    <h1 class="brand">Rankwell</h1>
    <p class="intro">Discover how people are ranked in your company!<br>Login or register now.</p>
    <form class="login-form">
      <div class="field">Email Address</div>
      <div class="field">Password</div>
      <div class="sign-in">Sign In</div>
    </form>
  </section>

  <ol class="ranking">
    <li class="rank-row">
      <div class="rank-badge"><span class="rank-num">1<em>st</em></span><div class="avatar" role="img" aria-label="Portrait photo of Leo Marsh"></div></div>
      <div class="person"><h2>Leo Marsh</h2><p>Points: <b>15</b><br>No. of reviews: <b>1</b></p></div>
      <dl class="ratings">
        <div class="rating"><dt>Smart:</dt><dd class="stars"><svg class="on"><use href="#star"/></svg><svg class="on"><use href="#star"/></svg><svg class="on"><use href="#star"/></svg><svg class="on"><use href="#star"/></svg><svg class="on"><use href="#star"/></svg></dd></div>
        <div class="rating"><dt>Easy to work with:</dt><dd class="stars"><svg class="on"><use href="#star"/></svg><svg class="on"><use href="#star"/></svg><svg class="on"><use href="#star"/></svg><svg class="on"><use href="#star"/></svg><svg class="on"><use href="#star"/></svg></dd></div>
        <div class="rating"><dt>Hard worker:</dt><dd class="stars"><svg class="on"><use href="#star"/></svg><svg class="on"><use href="#star"/></svg><svg class="on"><use href="#star"/></svg><svg class="on"><use href="#star"/></svg><svg class="on"><use href="#star"/></svg></dd></div>
      </dl>
    </li>
    <li class="rank-row">
      <div class="rank-badge"><span class="rank-num">2<em>nd</em></span><div class="avatar" role="img" aria-label="Portrait photo of Daniel Ashworth"></div></div>
      <div class="person"><h2>Daniel Ashworth</h2><p>Points: <b>12</b><br>No. of reviews: <b>1</b></p></div>
      <dl class="ratings">
        <div class="rating"><dt>Smart:</dt><dd class="stars"><svg class="on"><use href="#star"/></svg><svg class="on"><use href="#star"/></svg><svg class="on"><use href="#star"/></svg><svg class="on"><use href="#star"/></svg><svg class="off"><use href="#star"/></svg></dd></div>
        <div class="rating"><dt>Easy to work with:</dt><dd class="stars"><svg class="on"><use href="#star"/></svg><svg class="on"><use href="#star"/></svg><svg class="on"><use href="#star"/></svg><svg class="on"><use href="#star"/></svg><svg class="off"><use href="#star"/></svg></dd></div>
        <div class="rating"><dt>Hard worker:</dt><dd class="stars"><svg class="on"><use href="#star"/></svg><svg class="on"><use href="#star"/></svg><svg class="on"><use href="#star"/></svg><svg class="on"><use href="#star"/></svg><svg class="on"><use href="#star"/></svg></dd></div>
      </dl>
    </li>
    <li class="rank-row">
      <div class="rank-badge"><span class="rank-num">3<em>rd</em></span><div class="avatar" role="img" aria-label="Portrait photo of Owen Fletcher"></div></div>
      <div class="person"><h2>Owen Fletcher</h2><p>Points: <b>8</b><br>No. of reviews: <b>1</b></p></div>
      <dl class="ratings">
        <div class="rating"><dt>Smart:</dt><dd class="stars"><svg class="on"><use href="#star"/></svg><svg class="on"><use href="#star"/></svg><svg class="on"><use href="#star"/></svg><svg class="off"><use href="#star"/></svg><svg class="off"><use href="#star"/></svg></dd></div>
        <div class="rating"><dt>Easy to work with:</dt><dd class="stars"><svg class="on"><use href="#star"/></svg><svg class="on"><use href="#star"/></svg><svg class="on"><use href="#star"/></svg><svg class="on"><use href="#star"/></svg><svg class="off"><use href="#star"/></svg></dd></div>
        <div class="rating"><dt>Hard worker:</dt><dd class="stars"><svg class="on"><use href="#star"/></svg><svg class="on"><use href="#star"/></svg><svg class="on"><use href="#star"/></svg><svg class="on"><use href="#star"/></svg><svg class="off"><use href="#star"/></svg></dd></div>
      </dl>
    </li>
  </ol>
</main>
</body>
</html>
```